CORE 303 fitness page promoting new gym in Dania beach, FL

The purpose of the website is to attract new members to our new fitness facility opening in Dania beach, Florida. The city lacks places for functional training so we want to target this market of adult/young adult fitness personal. Not just meant for fitness buffs, first timers are encouraged to begin their health/fitness journey with us. Family owned, providing a combination of fitness services include personal and small group strength training, large group fitness classes with the use of sleds, dumbbells, kettlebells, medicine balls, cones, hurdles, ladders, and punching bags. Smoothie bar inside as well. Need to deliver a clear message of what kind of workouts we do, the people we want to attract, and how to sign up. Also make it known that we have showers on site (very rare to find in fitness studios).
Target Market(s)
Fit, health conscious, business professionals
Industry/Entity Type
Fitness
Number of Pages Required
3 page
Requirements
Must have
- Bright colors that scream SIGN UP, Would like to see logo in large, a big attractive sign saying First class is free. The concept of the gym is that we educate our clients on fitness rather than throwing them blindly into working out. We want our layout to mimic a schools idea of having a curriculum (styles of class/schedule) a tuition (membership costs).
Nice to have
- Big images that promote the gym, option to have video on front page displaying workouts.

```html
<!DOCTYPE html>
<html lang="en">
<head>
<meta charset="utf-8">
<title>CORE 303 — Functional Training Studio</title>
<link rel="stylesheet" href="https://fonts.googleapis.com/css2?family=Lato:wght@300;400;700;900&display=swap">
<style>
:root{
  --pink:#e3197e;
  --yellow:#ede52a;
  --blue:#1f86cc;
  --cyan:#2fb3e6;
  --black:#0b0b0b;
  --ink:#1c1c1c;
  --grey:#8a8a8a;
  --tile-yellow:#d2cb18;
  --tile-pink:#c91c79;
  --tile-blue:#2590d8;
  --white:#ffffff;
}
*{box-sizing:border-box;margin:0;padding:0}
html,body{width:1200px;height:3377px;overflow:hidden}
body{font-family:"Lato",Arial,sans-serif;background:var(--white);color:var(--ink);position:relative}
.abs{position:absolute}

/* header */
.hero{position:absolute;left:0;top:0;width:1200px;height:799px;
  background:radial-gradient(ellipse at 55% 40%,#4a4540 0%,#23201e 45%,#0a0a0a 85%)}
.nav-band{position:absolute;top:0;left:0;width:1200px;height:88px}
.nav{position:absolute;top:0;left:356px;height:88px;display:flex;align-items:center;gap:44px;color:var(--white);font-size:16px}
.nav .social{display:flex;gap:10px}
.nav .social span{width:32px;height:32px;border:2px solid var(--white);border-radius:50%}
.nav-signup{position:absolute;top:0;left:1000px;height:88px;line-height:88px;color:var(--blue);font-weight:900;font-size:27px}
.brand{position:absolute;left:98px;top:96px;display:flex;align-items:center;gap:10px}
.brand-mark{width:20px;height:20px;background:var(--pink)}
.brand-name{font-weight:900;font-size:36px;color:var(--pink);letter-spacing:1px;line-height:1}
.hero-title{position:absolute;top:382px;left:0;width:1200px;text-align:center;color:var(--white);font-weight:900;font-size:84px;letter-spacing:-1px}
.hero-copy{position:absolute;top:494px;left:230px;width:740px;text-align:center;color:var(--white);font-size:15px;line-height:33px;font-weight:700}
.play{position:absolute;left:562px;top:578px}

/* sign up bar */
.signup-bar{position:absolute;left:0;width:1200px;height:83px}
.signup-bar.dark{top:799px;background:var(--black)}
.signup-bar.blue{top:2199px;background:var(--blue)}
.signup-title{position:absolute;left:100px;top:0;line-height:83px;color:var(--yellow);font-weight:900;font-size:30px;white-space:nowrap}
.email-field{position:absolute;left:563px;top:19px;width:402px;height:45px;background:var(--white);border-radius:23px;padding-left:28px;line-height:45px;font-size:13px;color:#777}
.signup-btn{position:absolute;left:975px;top:19px;width:124px;height:45px;border-radius:23px;background:var(--pink);color:var(--white);text-align:center;line-height:45px;font-size:15px;font-weight:700}

/* what we do */
.section-title{position:absolute;top:982px;left:0;width:1200px;text-align:center;font-size:42px;font-weight:300;color:var(--ink)}
.section-title b{font-weight:900}
.services{position:absolute;left:101px;top:1085px;width:998px;height:369px;display:grid;grid-template-columns:repeat(4,1fr);grid-template-rows:repeat(2,1fr)}
.tile{position:relative;display:flex;flex-direction:column;align-items:center;justify-content:center;color:var(--white);font-weight:700;font-size:15px;text-transform:uppercase}
.tile svg{margin-bottom:22px}
.tile.yellow{background:var(--tile-yellow)}
.tile.pink{background:var(--tile-pink)}
.tile.blue{background:var(--tile-blue)}
.tile.photo-a{background:linear-gradient(160deg,#4a4a4a,#1f1f1f)}
.tile.photo-b{background:linear-gradient(200deg,#3a3a3a,#0f0f0f)}
.carousel-arrow{position:absolute;top:1238px}

/* mission */
.mission{position:absolute;top:1569px;left:0;width:1200px;height:630px;background:#f4f4f4}
.mission-photo{position:absolute;left:0;top:0;width:645px;height:630px;
  background:linear-gradient(120deg,#3a3f3a 0%,#6b7b6a 40%,#a84a3c 70%,#cfd3cf 100%);
  clip-path:polygon(0 0,608px 0,645px 630px,0 630px)}
.mission-rule{position:absolute;left:691px;top:1686px;width:44px;height:4px;background:var(--blue)}
.mission-title{position:absolute;left:691px;top:1706px;font-weight:900;font-size:42px;color:var(--ink)}
.mission-copy{position:absolute;left:691px;top:1780px;width:420px;font-size:13.5px;line-height:37px;color:var(--grey)}
.read-more{position:absolute;left:691px;top:2039px;width:130px;height:40px;border-radius:20px;background:var(--pink);color:var(--white);font-size:13px;font-weight:900;text-align:center;line-height:40px}

/* amenities */
.amenity{position:absolute;top:2397px;width:485px;height:355px}
.amenity.smoothie{left:99px;background:linear-gradient(135deg,#8a6a4a,#d9c2a0 45%,#e06a2a 80%,#5a3a2a)}
.amenity.showers{left:614px;background:linear-gradient(135deg,#c7a47a,#e8dfd2 45%,#8a7a6a 80%,#4a3e34)}
.amenity-label{position:absolute;left:0;top:135px;width:100%;height:90px;background:rgba(255,255,255,.82);text-align:center;line-height:90px;font-weight:700;font-size:35px;color:var(--pink)}

/* footer */
.footer{position:absolute;top:2865px;left:0;width:1200px;height:512px;background:var(--black)}
.foot-head{position:absolute;top:2940px;font-weight:700;font-size:14px;color:var(--white)}
.foot-rule{position:absolute;top:2975px;width:48px;height:4px;background:var(--yellow)}
.contact-list{position:absolute;left:146px;top:3015px;width:260px;font-size:12px;line-height:19px;list-style:none;color:var(--white)}
.contact-list li{display:flex;gap:16px;margin-bottom:18px}
.contact-list svg{flex:none;margin-top:2px}
.hours{position:absolute;left:493px;top:3004px;font-size:12px;line-height:23.5px;list-style:none;color:var(--white)}
.foot-brand{position:absolute;left:783px;top:3000px;width:300px;display:flex;flex-direction:column;align-items:center}
.foot-brand .brand-mark{width:30px;height:30px;margin-bottom:14px}
.foot-brand .brand-name{font-size:60px;color:var(--cyan)}
.foot-social{position:absolute;left:431px;top:3231px;display:flex;gap:14px}
.foot-social span{width:36px;height:36px;border:2px solid var(--white);border-radius:50%}
.copyright{position:absolute;left:99px;top:3326px;width:1000px;height:51px;background:var(--yellow);color:var(--ink);text-align:center;line-height:51px;font-size:13px}
</style>
</head>
<body>

<section class="hero" role="img" aria-label="Athlete lifting dumbbells on a gym floor in low light"></section>

<header class="nav-band">
  <svg class="abs" style="left:0;top:0" width="1200" height="88" aria-hidden="true">
    <polygon points="281,0 930,0 950,88 322,88" fill="var(--pink)"/>
    <polygon points="930,0 1200,0 1200,88 950,88" fill="var(--yellow)"/>
  </svg>
  <nav class="nav">
    <span>Curriculum</span><span>Hours</span><span>Mission</span><span>Schedule</span><span>Tution</span>
    <span class="social"><span aria-label="Social profile"></span><span aria-label="Social profile"></span></span>
  </nav>
  <div class="nav-signup">SIGN UP</div>
</header>

<div class="brand">
  <span class="brand-mark"></span><span class="brand-name">CORE 303</span>
</div>

<h1 class="hero-title">FIRST CLASS IS FREE!</h1>
<p class="hero-copy">Sed ut perspiciatis unde omnis iste natus error sit voluptatem accusantium doloremque laudantium, totam rem aperiam, eaque ipsa quae ab illo inventore veritatis et quasi architecto beatae vitae dicta</p>
<svg class="play" width="76" height="76" aria-label="Play workout video">
  <circle cx="38" cy="38" r="35" fill="none" stroke="#fff" stroke-width="3"/>
  <polygon points="29,22 55,38 29,54" fill="#fff"/>
</svg>

<div class="signup-bar dark">
  <div class="signup-title">SIGN UP NOW CORE303GYM</div>
  <div class="email-field">Enter Email</div>
  <div class="signup-btn">SIGN UP</div>
</div>

<h2 class="section-title"><b>WHAT</b> WE DO</h2>
<svg class="carousel-arrow" style="left:28px" width="30" height="68" aria-label="Previous"><polyline points="28,2 2,34 28,66" fill="none" stroke="#aaa" stroke-width="2"/></svg>
<svg class="carousel-arrow" style="left:1142px" width="30" height="68" aria-label="Next"><polyline points="2,2 28,34 2,66" fill="none" stroke="#aaa" stroke-width="2"/></svg>

<div class="services">
  <div class="tile yellow">
    <svg width="84" height="40" fill="none" stroke="#fff" stroke-width="4"><line x1="6" y1="20" x2="78" y2="20"/><rect x="16" y="6" width="8" height="28"/><rect x="60" y="6" width="8" height="28"/></svg>
    Barbells
  </div>
  <div class="tile pink">
    <svg width="70" height="60" fill="none" stroke="#fff" stroke-width="4"><line x1="4" y1="12" x2="66" y2="12"/><rect x="18" y="4" width="34" height="54"/><line x1="18" y1="30" x2="52" y2="30"/></svg>
    Squat Racks
  </div>
  <div class="tile blue">
    <svg width="50" height="56" fill="none" stroke="#fff" stroke-width="4"><path d="M14 20 Q14 4 25 4 Q36 4 36 20"/><circle cx="25" cy="36" r="17"/></svg>
    Kettlebells
  </div>
  <div class="tile photo-a" role="img" aria-label="Group class training with kettlebells"></div>
  <div class="tile photo-b" role="img" aria-label="Athlete doing a dumbbell curl"></div>
  <div class="tile blue">
    <svg width="60" height="60" fill="none" stroke="#fff" stroke-width="4"><line x1="18" y1="2" x2="18" y2="30"/><line x1="42" y1="2" x2="42" y2="30"/><circle cx="16" cy="45" r="11"/><circle cx="44" cy="45" r="11"/></svg>
    Battleropes
  </div>
  <div class="tile yellow">
    <svg width="64" height="56" fill="none" stroke="#fff" stroke-width="4"><line x1="4" y1="52" x2="60" y2="52"/><line x1="48" y1="52" x2="48" y2="6"/><line x1="48" y1="6" x2="58" y2="2"/><path d="M12 44 L40 44 L30 28 Z"/></svg>
    Cardio Machines
  </div>
  <div class="tile pink">
    <svg width="60" height="58" fill="none" stroke="#fff" stroke-width="4"><path d="M20 12 Q20 2 30 2 Q40 2 40 12"/><rect x="8" y="12" width="44" height="42" rx="10"/><line x1="8" y1="30" x2="52" y2="30"/></svg>
    Aqua Training Bags
  </div>
</div>

<section class="mission">
  <div class="mission-photo" role="img" aria-label="Woman in red leggings resting by a bright window"></div>
</section>
<div class="mission-rule"></div>
<h2 class="mission-title">MISSION</h2>
<p class="mission-copy">Functional training studio seeking to go the extra mile with our clients through educating them on their movements to ensure the proper form and execution. You can work out every part of your body, but do you really know what you're doing or why? Core 303 aims to educate our clients. Teach them how to teach themselves and train the right way with real results. Educate their bodies.</p>
<div class="read-more">READ MORE</div>

<div class="signup-bar blue">
  <div class="signup-title">SIGN UP NOW CORE303GYM</div>
  <div class="email-field">Enter Email</div>
  <div class="signup-btn">SIGN UP</div>
</div>

<div class="amenity smoothie" role="img" aria-label="Two members smiling at the smoothie bar">
  <div class="amenity-label">SMOOTHIE BAR</div>
</div>
<div class="amenity showers" role="img" aria-label="Clean on-site shower stalls">
  <div class="amenity-label">SHOWERS</div>
</div>

<footer class="footer"></footer>
<div class="foot-head" style="left:146px">CONTACT INFO</div>
<div class="foot-rule" style="left:146px"></div>
<ul class="contact-list">
  <li><svg width="14" height="16" viewBox="0 0 14 16"><path d="M7 0a6 6 0 0 1 6 6c0 4-6 10-6 10S1 10 1 6a6 6 0 0 1 6-6z" fill="#fff"/><circle cx="7" cy="6" r="2" fill="#000"/></svg><span>17-21 Sed ut perspiciatis unde omnis iste natus errorsit accusantium.</span></li>
  <li><svg width="14" height="14" viewBox="0 0 14 14"><path d="M3 0l3 3-2 2c1 2 3 4 5 5l2-2 3 3-2 3C6 14 0 8 0 3z" fill="#fff"/></svg><span>Phone: 555-014-2290</span></li>
  <li><svg width="14" height="11" viewBox="0 0 14 11"><rect width="14" height="11" fill="#fff"/><polyline points="0,0 7,6 14,0" fill="none" stroke="#000" stroke-width="1.5"/></svg><span>Email: hello@core303studio.com</span></li>
</ul>

<div class="foot-head" style="left:493px">OPERATING BUSINESS HOURS</div>
<div class="foot-rule" style="left:493px"></div>
<ul class="hours">
  <li>Monday: 6:00 am – 8:30 pm</li>
  <li>Tuesday: 6:00 am – 8:30 pm</li>
  <li>Wednesday: 6:00 am – 8:30 pm</li>
  <li>Thursday: 6:00 am – 8:30 pm</li>
  <li>Friday: 6:00 am – 7:15 pm</li>
  <li>Saturday: 8:00 am – 10:15 am</li>
  <li>Sunday: 9:00 am – 11:15 am</li>
</ul>

<div class="foot-brand">
  <span class="brand-mark"></span>
  <span class="brand-name">CORE 303</span>
</div>

<div class="foot-social" aria-label="Social profiles">
  <span></span><span></span><span></span><span></span><span></span><span></span><span></span>
</div>

<div class="copyright">©2018 Core303studio.com All Rights Reserved.&nbsp; Privacy Policy &nbsp;|&nbsp; Terms and Use</div>

</body>
</html>
```